Business card for massage therapy company called Brook Fern Wellness

Need business card for massage therapy company called Brook Fern Wellness. Would like my logo on the front and the back of the card I have 3 options of logos and you can play with what looks better.

Would like this information displayed on the back of the card:

Marcus Ellery
Licensed Massage Therapist
321-555-0147
brookfern-example.com
brookfern_rest_

```html
<!DOCTYPE html>
<html lang="en">
<head>
<meta charset="utf-8">
<title>Brook Fern Wellness – Business Card</title>
<link rel="stylesheet" href="https://fonts.googleapis.com/css2?family=Marcellus&family=Mulish:wght@400;700&display=swap">
<style>
  :root {
    --sage: #5a7550;
    --paper: #ffffff;
    --ink: #111111;
    --edge: #c8c8c8;
  }
  * { margin: 0; padding: 0; box-sizing: border-box; }
  html, body {
    width: 1200px;
    height: 362px;
    overflow: hidden;
    background: var(--paper);
  }
  .card-spread {
    position: relative;
    width: 1200px;
    height: 362px;
  }
  .card-front {
    position: absolute;
    left: 0; top: 0;
    width: 598px; height: 362px;
    background: var(--sage);
    color: var(--paper);
  }
  .card-back {
    position: absolute;
    left: 598px; top: 0;
    width: 602px; height: 362px;
    background: var(--paper);
    border: 1px solid var(--edge);
    color: var(--ink);
  }
  .brand-ring {
    position: absolute;
    display: block;
  }
  .card-front .brand-ring { left: 234px; top: 70px; }
  .card-back .brand-ring { left: 274px; top: 57px; }
  .brand-name {
    position: absolute;
    left: 0; right: 0;
    text-align: center;
    font-family: "Marcellus", serif;
    font-weight: 400;
    line-height: 1;
    white-space: nowrap;
  }
  .card-front .brand-name { color: var(--paper); }
  .card-back .brand-name { color: var(--sage); }
  .card-front .brand-name-main { top: 236px; font-size: 40px; letter-spacing: 0.5px; }
  .card-front .brand-name-sub  { top: 280px; font-size: 23px; letter-spacing: 7px; padding-left: 7px; }
  .card-back .brand-name-main  { top: 112px; font-size: 20px; letter-spacing: 0.5px; }
  .card-back .brand-name-sub   { top: 133px; font-size: 10px; letter-spacing: 3px; padding-left: 3px; }
  .contact-block {
    position: absolute;
    left: 0; right: 0; top: 178px;
    text-align: center;
    font-family: "Mulish", sans-serif;
    line-height: 1;
  }
  .therapist-name {
    font-size: 24px;
    font-weight: 700;
    margin-bottom: 6px;
  }
  .therapist-title {
    font-size: 19px;
    font-weight: 400;
    margin-bottom: 31px;
  }
  .contact-line {
    font-size: 19px;
    font-weight: 400;
    margin-bottom: 6px;
  }
</style>
</head>
<body>
  <main class="card-spread">
    <section class="card-front">
      <svg class="brand-ring" width="132" height="132" viewBox="0 0 132 132" aria-hidden="true">
        <circle cx="66" cy="66" r="64" fill="none" stroke="var(--paper)" stroke-width="2"/>
      </svg>
      <p class="brand-name brand-name-main">BROOK FERN</p>
      <p class="brand-name brand-name-sub">WELLNESS</p>
    </section>

    <section class="card-back">
      <svg class="brand-ring" width="54" height="54" viewBox="0 0 54 54" aria-hidden="true">
        <circle cx="27" cy="27" r="26" fill="none" stroke="var(--sage)" stroke-width="1.2"/>
      </svg>
      <p class="brand-name brand-name-main">BROOK FERN</p>
      <p class="brand-name brand-name-sub">WELLNESS</p>

      <div class="contact-block">
        <p class="therapist-name">Marcus Ellery</p>
        <p class="therapist-title">Licensed Massage Therapist</p>
        <p class="contact-line">321-555-0147</p>
        <p class="contact-line">brookfern-example.com</p>
        <p class="contact-line">brookfern_rest_</p>
      </div>
    </section>
  </main>
</body>
</html>
```